Blue Heron Courier & Delivery Services needs a flyer

We need an introductory flyer for a new company based in Yellowknife, Northwest Territories,Canada. Our company name is Blue Heron Courier & Delivery Services. We will be handling envelopes and small packages up to 20 pounds. We expect 20 percent of our business to come from residential customers and 80 percent from the business community including lawyers, doctors, engineers and government offices. The main message that we will try to convey in this flyer is that we are a new and exciting company that promises to make 100% customer satisfaction our number one goal. I would like the layout to be elegant and simple and certainly not cluttered. It will be a single sided flyer. Text should be easy to read and most likely at most two fonts. I would like one stunning image or photo relating to the courier business and message. There should be plenty of white space throughout the flyer and nice margins on all sides. I would like my flyer to be 8.5 inches by 11 inches and it should read from top to bottom. . I would like a nice big bold headline that in some way mentions " Special Offer- Up to 100% Off. You can change the wording if you have a better idea. Throughout the flyer you can highlight and italicize for emphasis. Please try to use bullet points for my five main reasons for hiring our company which are: you will be 100% satisfied with each delivery or you will be given a complete refund no questions asked, your envelope or package will be delivered on time every time, you will always be treated throughout the delivery process in a professional manner, you will be given the widest selection in Yellowknife of price points and delivery options , you can trust us with your most important and time sensitive deliveries. Try to incorporate something next to these five points to really draw attention like a check mark, star etc.... I would prefer if my company name and contact info is in the bottom third of the flyer. My email is blueheroncourieryk@mailbox-example.net. My phone number is 867-312-7794. It might be a good idea to have my phone number also at the top of the flyer someplace after the headline saying like Call Now!!! you can use boxes, borders and contrasting bold colors to bring flyer to life. I have a testimonial from a business owner that I dealt with when I ran another business which would be nice to have included . " While receiving daily deliveries for 18 years from Calvin Marsh I found him to be punctual , reliable and efficient " Glen Potter, owner of Potter and Lindqvist Trading LTD, Yellowknife,NWT. I thought perhaps at the top of flyer after the headline perhaps in some way you could say Yellowknife's newest and best courier and delivery service is pleased to offer the following stunning discounts: then you could list the three special offers: 1) First 5 businesses to book regular scheduled deliveries will get 100% off their first delivery. 2) First 5 businesses to book a single delivery will get 50% off that delivery. 3) First 5 residential customers to book a delivery will receive 25% off that delivery. I thought you could mention my name somewhere. Calvin Marsh. Owner has lived in Yellowknife for 42 years and has 20 years experience doing performing important and time sensitive deliveries. Perhaps you could mention somewhere that we will have a couple of ongoing discounts also which will be 1) seniors discounts. 2) regular scheduled deliveries discounts. I have suggested colors but if you have other ideas I would certainly look at them. Our business tag line is. On Time Every Time
Target Market(s)
Business owners typically males 30-50 years old
Industry/Entity Type
Delivery Service
Requirements
Must have
- Done in CMYK mode sufficient bleed size for printing
Nice to have
- Nothing set in stone. I recently had my logo design uploaded to this brief. It is up to you if you feel it should be included in the flyer.
Should not have
- I am willing to look at any design

```html
<!DOCTYPE html>
<html lang="en">
<head>
<meta charset="utf-8">
<title>Blue Heron Courier &amp; Delivery Services – Flyer</title>
<link href="https://fonts.googleapis.com/css2?family=Roboto+Condensed:wght@400&family=Open+Sans:wght@400;600&display=swap" rel="stylesheet">
<style>
  :root{
    --page-bg:#e9e9e7;
    --paper:#ffffff;
    --orange:#f07c2e;
    --orange-deep:#e4691c;
    --burst-red:#a3101a;
    --burst-red-light:#d0262c;
    --panel-sage:#dbe0cc;
    --tag-green:#7aa63a;
    --tag-green-dark:#5e8a25;
    --ink-olive:#3b4520;
    --ink-brown:#8e3510;
    --ink-dark:#4a2a12;
    --band-green:#4f7a1e;
    --frame-grey:#9a9a9a;
  }
  *{box-sizing:border-box;margin:0;padding:0}
  html,body{width:1200px;height:1000px;overflow:hidden}
  body{background:var(--page-bg);font-family:"Open Sans",Verdana,sans-serif;position:relative}

  .flyer{position:absolute;left:240px;top:30px;width:720px;height:940px;background:var(--paper);overflow:hidden;box-shadow:0 2px 8px rgba(0,0,0,.18)}

  .header-band{position:absolute;left:0;top:0;width:720px;height:170px;background:var(--orange)}
  .company-name{position:absolute;left:40px;top:18px;font-family:"Roboto Condensed","Arial Narrow",sans-serif;font-weight:400;color:#fff;font-size:58px;line-height:72px;white-space:nowrap;transform:scaleX(.8);transform-origin:left top}
  .header-rule{position:absolute;left:40px;right:200px;top:156px;height:1px;background:rgba(255,255,255,.7)}

  .offer-burst{position:absolute;left:527px;top:-4px;width:194px;height:190px}
  .offer-burst svg{position:absolute;inset:0}
  .offer-burst-text{position:absolute;left:0;top:8px;width:194px;text-align:center;color:#fff;font-size:33px;line-height:43px}

  .hero-photo{position:absolute;left:0;top:170px;width:520px;height:190px;background:linear-gradient(90deg,#f4f4f4 0%,#e6e6e6 55%,#d9cfc2 80%,#f2f2f2 100%)}
  .satisfaction-box{position:absolute;left:5px;top:176px;width:280px;height:110px;background:var(--orange);border:3px solid var(--frame-grey);color:#fff;font-size:20px;line-height:42px;text-align:center;padding-top:10px}

  .call-block{position:absolute;left:500px;top:212px;width:205px;text-align:right}
  .call-block svg{width:40px;height:28px}
  .call-number{color:var(--orange);font-size:29px;line-height:36px;letter-spacing:.3px}

  .reasons-panel{position:absolute;left:5px;top:367px;width:707px;height:198px;background:var(--panel-sage)}
  .reasons-list{list-style:none;position:absolute;left:14px;top:4px;right:10px}
  .reasons-list li{position:relative;padding-left:26px;color:var(--ink-olive);font-size:16.6px;letter-spacing:.2px;line-height:28.6px}
  .reasons-list li svg{position:absolute;left:0;top:9px;width:20px;height:14px}
  .reasons-list .wide{padding-right:150px;white-space:nowrap}
  .reasons-tag{position:absolute;left:544px;top:373px;width:176px;height:57px}
  .tag-label{position:absolute;inset:0;color:#fff;display:flex;align-items:center;justify-content:flex-end;padding-right:6px}
  .reasons-tag .tag-label{font-size:32px}

  .courier-figure{position:absolute;left:200px;top:595px;width:240px;height:345px;opacity:.35;background:radial-gradient(ellipse at 50% 40%,#c9b49a 0%,#d8cfc3 45%,rgba(255,255,255,0) 75%)}

  .offers{position:absolute;left:21px;top:582px;width:670px;color:var(--ink-brown)}
  .offers-title{font-size:19px;line-height:28px;font-weight:400}
  .offers-list{list-style:none;font-size:21.5px;letter-spacing:.3px;line-height:28.6px}
  .offers-list li{padding-left:31px;text-indent:-31px}

  .discounts-tag{position:absolute;left:540px;top:767px;width:180px;height:34px}
  .discounts-tag .tag-label{font-size:20px;padding-right:14px}
  .discounts-panel{position:absolute;left:15px;top:803px;width:697px;height:70px;background:var(--panel-sage);color:var(--ink-brown);font-size:21px;letter-spacing:.5px;line-height:29px;padding:4px 0 0 15px;white-space:nowrap}

  .location{position:absolute;left:16px;top:872px;color:var(--ink-dark);font-size:20.5px;letter-spacing:.4px;line-height:28px}
  .email{position:absolute;right:10px;top:904px;color:var(--ink-brown);font-size:15px;line-height:20px}
  .footer-band{position:absolute;left:0;bottom:0;width:720px;height:16px;background:var(--band-green)}
</style>
</head>
<body>
<main class="flyer">
  <header class="header-band">
    <h1 class="company-name">BLUE HERON COURIER<br>&amp; &nbsp;DELIVERY &nbsp;SERVICES</h1>
    <div class="header-rule"></div>
  </header>

  <div class="offer-burst">
    <svg viewBox="0 0 194 190" aria-hidden="true">
      <defs><radialGradient id="burstFill" cx="50%" cy="40%" r="60%"><stop offset="0" stop-color="var(--burst-red-light)"/><stop offset="1" stop-color="var(--burst-red)"/></radialGradient></defs>
      <polygon fill="url(#burstFill)" points="192,95 175.5,110.6 184.8,131.4 163.5,139.5 164.2,162.2 141.5,161.5 133.4,182.8 112.6,173.5 97,190 81.4,173.5 60.6,182.8 52.5,161.5 29.8,162.2 30.5,139.5 9.2,131.4 18.5,110.6 2,95 18.5,79.4 9.2,58.6 30.5,50.5 29.8,27.8 52.5,28.5 60.6,7.2 81.4,16.5 97,0 112.6,16.5 133.4,7.2 141.5,28.5 164.2,27.8 163.5,50.5 184.8,58.6 175.5,79.4"/>
    </svg>
    <p class="offer-burst-text">Special<br>Offer<br>Up to<br>100%</p>
  </div>

  <div class="hero-photo" role="img" aria-label="Photo of a white delivery truck and a courier in uniform beside a hand truck stacked with cardboard boxes"></div>
  <div class="satisfaction-box">100% customer<br>satisfication</div>

  <div class="call-block">
    <svg viewBox="0 0 40 28" aria-hidden="true"><path fill="var(--orange)" d="M4 9c0-4 7-7 16-7s16 3 16 7v3h-8V8c-2-1-5-1.5-8-1.5S14 7 12 8v4H4z"/><rect x="9" y="13" width="22" height="13" rx="3" fill="var(--orange)"/><circle cx="20" cy="19.5" r="3.5" fill="#fff"/></svg>
    <p class="call-number">867-312-7794</p>
  </div>

  <section class="reasons-panel">
    <ul class="reasons-list">
      <li class="wide"><svg viewBox="0 0 20 14"><path fill="var(--orange)" d="M0 0l20 7-20 7 5-7z"/></svg>you will be 100% satisfied with each delivery or<br>you will be given a complete refund no questions asked,</li>
      <li><svg viewBox="0 0 20 14"><path fill="var(--orange)" d="M0 0l20 7-20 7 5-7z"/></svg>your envelope or package will be delivered on time every time,</li>
      <li><svg viewBox="0 0 20 14"><path fill="var(--orange)" d="M0 0l20 7-20 7 5-7z"/></svg>you will be treated throughout the delivery process in a professional &nbsp;manner,</li>
      <li><svg viewBox="0 0 20 14"><path fill="var(--orange)" d="M0 0l20 7-20 7 5-7z"/></svg>you will be given the widest selection in Yellowknife of price points and delivery<br>options ,</li>
      <li><svg viewBox="0 0 20 14"><path fill="var(--orange)" d="M0 0l20 7-20 7 5-7z"/></svg>you can trust us with your most important and time sensitive deliveries.</li>
    </ul>
  </section>
  <div class="reasons-tag">
    <svg viewBox="0 0 176 57" width="176" height="57" aria-hidden="true"><defs><linearGradient id="tagGreen" x1="0" y1="0" x2="0" y2="1"><stop offset="0" stop-color="var(--tag-green)"/><stop offset="1" stop-color="var(--tag-green-dark)"/></linearGradient></defs><polygon fill="url(#tagGreen)" points="0,28.5 22,0 176,0 176,57 22,57"/></svg>
    <span class="tag-label">5 OFFER</span>
  </div>

  <div class="courier-figure" role="img" aria-label="Faded photo of a running courier carrying a parcel"></div>

  <section class="offers">
    <h2 class="offers-title">THREE SPECIAL OFFER</h2>
    <ol class="offers-list">
      <li>1) First 5 businesses to book regular scheduled deliveries will get 100% off their first delivery.</li>
      <li>2) First 5 businesses to book a single delivery will get 50% off that delivery.</li>
      <li>3) First 5 residential customers to book a delivery will receive 25% off that delivery.</li>
    </ol>
  </section>

  <div class="discounts-tag">
    <svg viewBox="0 0 180 34" width="180" height="34" aria-hidden="true"><polygon fill="url(#tagGreen)" points="0,17 18,0 180,0 180,34 18,34"/></svg>
    <span class="tag-label">DISCOUNTS</span>
  </div>
  <section class="discounts-panel">
    <p>we will have a couple of ongoing discounts also which will be<br>&nbsp;1) seniors discounts. 2) regular scheduled deliveries discounts.</p>
  </section>

  <p class="location">Yellowknife, Northwest Territories,Canada.</p>
  <p class="email">blueheroncourieryk@mailbox-example.net</p>
  <div class="footer-band"></div>
</main>
</body>
</html>
```